World leading Water filters German made

I am a local Plumbing business who is authorised water filter installer
I want to do a Flyer design double sided targeting niche market for Water Filters.
My company colours are black background with white writing.
( but happy to go into different colours to capture more people )
I want all my stuff, sleek and professional with the same fonts throughout.
Www.brightvalepipeworks.au
Is my website you can see how I do things there.
I want the local business awards finalist logo on the flyer too ( it’ll be in the photo)
This Flyer I want all about health and wellness making big points on water filtration benefits
Massive to included HYDROGEN WATER AND ALKALINE WATER ,
REMOVE FLUORIDE
I don’t know whether to have it with the pre-save branded information I sent over, but I don’t want the company other companies name everywhere
I want the main focus about my company Brightvale Pipeworks And Boiler Experts
I want the focus to be about a family owned and run Illawarra local business establish for over 20 years.
Please note I have included a Customer brochure the company has designed so you can see some key points on the second page about the products. I want this a lot more eye-catching and appealing please
Target Market(s)
Health and wellness people
Colors
Designer to choose colors to be used in the design.
Requirements
Must have
- Call Trevor 0438 627 195, my website , social media buttons ,
Nice to have
- World leading , health and wellness ,
Should not have
- Any information to lead them away from calling myself , I’m the authorities dealer for purestream supply but I want to no have as much anout them.

```html
<!DOCTYPE html>
<html lang="en">
<head>
<meta charset="utf-8">
<title>Brightvale Pipeworks – Double-sided Water Filtration Flyer</title>
<link href="https://fonts.googleapis.com/css2?family=Krona+One&family=Poppins:wght@400;500;600;700&display=swap" rel="stylesheet">
<style>
  :root{
    --sky-top:#bcdcf3;
    --sky-mid:#dcedf9;
    --sky-light:#f7fbfe;
    --brand-blue:#4aa8e0;
    --band-blue:#6bb8e6;
    --ink:#0b0b0d;
    --panel:#050607;
    --white:#ffffff;
    --muted:#d5dbe0;
    --rule:#4a4f55;
    --gold:#c9a24a;
    --gold-light:#ecd28c;
    --ribbon:#d3202a;
    --ribbon-dark:#a9151d;
    --stage:#d6d6d6;
  }
  *{box-sizing:border-box;margin:0;padding:0}
  html,body{width:800px;height:1200px;overflow:hidden;background:var(--stage)}
  .stage{position:relative;width:800px;height:1200px;overflow:hidden}

  .flyer{position:absolute;width:680px;height:880px;overflow:hidden;font-family:"Poppins",sans-serif;color:var(--ink);
    transform:scale(.65);transform-origin:0 0;box-shadow:0 10px 30px rgba(0,0,0,.35)}
  .flyer--front{left:179px;top:18px}
  .flyer--back{left:179px;top:610px}

  .hero{position:absolute;left:0;top:0;width:680px;height:440px;
    background:linear-gradient(160deg,var(--sky-top) 0%,var(--sky-mid) 45%,var(--sky-light) 100%)}
  .flyer--front .hero{height:490px}
  .panel{position:absolute;left:0;width:680px;background:var(--panel);color:var(--white)}
  .flyer--front .panel{top:490px;height:390px}
  .flyer--back .panel{top:440px;height:440px}

  .display{font-family:"Krona One",sans-serif;text-transform:uppercase}
  .blue{color:var(--brand-blue)}

  /* ---------- front ---------- */
  .hero-photo{position:absolute;left:300px;top:0;width:380px;height:490px;
    background:radial-gradient(ellipse 60% 45% at 45% 25%,#f2c56a 0%,#c6995a 30%,rgba(52,50,46,.95) 62%,#2b302d 80%,#3d5a50 100%);
    -webkit-mask-image:linear-gradient(90deg,transparent 0,#000 18%);mask-image:linear-gradient(90deg,transparent 0,#000 18%)}
  .brand-mark{position:absolute;left:48px;top:60px;display:flex;align-items:center;gap:10px;
    font-size:17px;line-height:1.15;color:var(--ink)}
  .brand-mark .square{width:14px;height:14px;background:var(--ink)}
  .front-headline{position:absolute;left:46px;top:146px;font-size:33px;line-height:33px;letter-spacing:.3px}

  .heritage-band{position:absolute;left:47px;top:340px;width:358px;height:100px;background:var(--band-blue);color:var(--white)}
  .heritage-text{position:absolute;left:17px;top:20px;font-size:13px;line-height:14px;font-weight:500;color:var(--ink)}
  .heritage-text strong{display:block;font-weight:700;text-transform:uppercase;font-size:13px;color:var(--white)}
  .years{position:absolute;left:140px;top:19px;line-height:1}
  .years small{display:block;font-size:7px;letter-spacing:1px;font-weight:600;color:var(--ink);padding-left:16px}
  .years .num{display:block;font-family:"Krona One",sans-serif;font-size:34px;line-height:36px;color:var(--white)}
  .years .label{display:block;font-family:"Krona One",sans-serif;font-size:14px;color:var(--white)}
  .award{position:absolute}
  .award--front{left:290px;top:328px}
  .award--back{left:574px;top:52px}

  .product--front{position:absolute;left:60px;top:-10px;width:275px;height:320px;
    background:linear-gradient(180deg,#e3e6e9 0%,#b4b9be 45%,#4b4f53 82%,#0b0c0d 100%);
    clip-path:polygon(0 14%,45% 0,100% 6%,100% 100%,0 100%)}
  .solution{position:absolute;left:364px;top:40px;width:300px}
  .solution h2{font-size:18px;line-height:21px;font-weight:400;color:var(--brand-blue)}
  .solution h2 b{color:var(--white);font-weight:700}
  .solution h2 .line2{display:block;color:var(--white);font-weight:700}
  .feature-list{list-style:none;margin-top:14px}
  .feature-list li{display:flex;align-items:center;gap:12px;font-size:12.5px;height:30px}
  .feature-list svg{flex:0 0 20px}

  /* ---------- shared footer ---------- */
  .call{position:absolute;left:40px;bottom:32px}
  .call .lead{font-size:18px;font-weight:500;line-height:20px}
  .call .number{display:flex;align-items:center;gap:6px;font-family:"Krona One",sans-serif;font-size:28px;line-height:34px;white-space:nowrap}
  .web-pill{position:absolute;left:345px;bottom:72px;width:278px;height:26px;border:1.5px solid var(--white);border-radius:14px;
    display:flex;align-items:center;justify-content:center;font-family:"Krona One",sans-serif;font-size:10px;letter-spacing:.3px}
  .distributor{position:absolute;left:345px;bottom:36px;line-height:1}
  .distributor .title{font-size:13px;font-weight:700}
  .distributor .sub{font-size:7px;font-weight:600;margin-top:2px}
  .social{position:absolute;left:520px;bottom:44px;display:flex;align-items:center;gap:5px;font-size:8px}
  .social .circle{width:11px;height:11px;border-radius:50%;background:var(--white)}

  /* ---------- back ---------- */
  .back-headline{position:absolute;left:48px;top:44px;font-size:33px;line-height:33px;letter-spacing:.3px}
  .service-area{position:absolute;left:80px;top:224px;font-size:11.5px;line-height:14px;font-weight:600;color:var(--ink)}
  .product--back{position:absolute;left:392px;top:64px;width:262px;height:360px;
    background:linear-gradient(180deg,#e7eaed 0%,#bfc4c8 40%,#6b7075 72%,#2a2d30 100%);
    clip-path:polygon(0 6%,100% 0,100% 100%,0 100%)}

  .why-band{position:absolute;left:47px;top:283px;width:348px;height:102px;background:var(--band-blue);display:flex}
  .why-tab{width:32px;background:var(--ink);color:var(--white);display:flex;align-items:center;justify-content:center}
  .why-tab span{transform:rotate(-90deg);white-space:nowrap;font-size:9px;font-weight:700;line-height:10px;text-align:center}
  .why-list{display:flex;list-style:none;padding:10px 0 0 6px;gap:0}
  .why-list li{width:62px;display:flex;flex-direction:column;align-items:center;text-align:center;
    font-size:6.8px;line-height:8px;font-weight:700;text-transform:uppercase;color:var(--ink)}
  .why-list .icon{width:32px;height:32px;border-radius:50%;background:var(--white);margin-bottom:8px;display:flex;align-items:center;justify-content:center}

  .benefit{position:absolute}
  .benefit h3{font-family:"Krona One",sans-serif;font-size:16px;line-height:18px;color:var(--brand-blue);text-transform:uppercase;margin-bottom:8px}
  .benefit .cols{display:flex;gap:14px}
  .benefit ul{list-style:none}
  .benefit li{position:relative;padding-left:12px;font-size:10.5px;line-height:12px;margin-bottom:2.5px}
  .benefit li::before{content:"";position:absolute;left:0;top:2px;width:7px;height:7px;border:1px solid var(--muted);border-radius:1px}
  .benefit li::after{content:"";position:absolute;left:2px;top:3px;width:3px;height:5px;border:solid var(--white);border-width:0 1.2px 1.2px 0;transform:rotate(40deg)}
  .benefit--health{left:50px;top:32px}
  .benefit--remove{left:364px;top:32px}
  .benefit--extend{left:50px;top:188px}
  .benefit--world{left:364px;top:188px}
  .benefit--health .cols ul:first-child{width:130px}
  .benefit--extend .cols ul:first-child{width:130px}
  .benefit--remove .cols ul:first-child{width:134px}
  .benefit--world .cols ul:first-child{width:134px}
  .divider{position:absolute;top:168px;height:0;border-top:1px dotted var(--rule)}
  .divider--left{left:50px;width:260px}
  .divider--right{left:364px;width:270px}
  .divider-v{position:absolute;left:330px;top:34px;height:300px;border-left:1px dotted var(--rule)}
</style>
</head>
<body>
<div class="stage">

  <!-- FRONT -->
  <article class="flyer flyer--front">
    <section class="hero">
      <div class="hero-photo" role="img" aria-label="Photo of a man in a dark hoodie drinking water from a bottle, with a waterfall blended into his body"></div>
      <div class="brand-mark display"><span class="square"></span><span>Brightvale<br>Pipeworks</span></div>
      <h1 class="front-headline display">
        <span class="blue">Brightvale<br>Pipeworks</span><br>
        <span>&amp; Boiler<br>Experts</span>
      </h1>
      <div class="heritage-band">
        <p class="heritage-text"><strong>Family owned</strong>&amp; run Illawarra<br>local business<br>establish</p>
        <div class="years"><small>FOR OVER</small><span class="num">20</span><span class="label">YEARS</span></div>
      </div>
      <svg class="award award--front" width="68" height="129" viewBox="0 0 68 129" aria-hidden="true">
        <rect x="0" y="0" width="68" height="129" fill="var(--ribbon)"/>
        <rect x="0" y="100" width="68" height="29" fill="var(--ribbon-dark)"/>
        <circle cx="34" cy="46" r="40" fill="var(--gold)"/>
        <circle cx="34" cy="46" r="31" fill="var(--gold-light)"/>
      </svg>
    </section>

    <section class="panel">
      <div class="product--front" role="img" aria-label="Product render of a stainless water filtration unit with three filter cartridges and a water splash"></div>
      <div class="solution">
        <h2>Your Complete <b>Home Water</b><span class="line2">Filtration German Solution:</span></h2>
        <ul class="feature-list">
          <li><svg width="20" height="22" viewBox="0 0 22 24" fill="none" stroke="var(--brand-blue)" stroke-width="1.6"><path d="M11 2C7 8 4 11 4 15a7 7 0 0 0 14 0c0-4-3-7-7-13z"/></svg>Hard water anti-scale protection</li>
          <li><svg width="20" height="22" viewBox="0 0 22 24" fill="none" stroke="var(--brand-blue)" stroke-width="1.6"><rect x="3" y="3" width="6" height="18"/><path d="M9 8h8M13 8v6M17 6v4"/></svg>Chemical removal</li>
          <li><svg width="20" height="22" viewBox="0 0 22 24" fill="none" stroke="var(--brand-blue)" stroke-width="1.6"><circle cx="11" cy="12" r="6"/><path d="M11 2v3M11 19v3M1 12h3M18 12h3M4 5l2 2M16 17l2 2M4 19l2-2M16 7l2-2"/></svg>Ultraviolet protection</li>
          <li><svg width="20" height="22" viewBox="0 0 22 24" fill="none" stroke="var(--brand-blue)" stroke-width="1.6"><circle cx="8" cy="14" r="6"/><circle cx="17" cy="6" r="3"/><circle cx="18" cy="18" r="2"/></svg>Hydrogen water &amp; alkaline water</li>
          <li><svg width="20" height="22" viewBox="0 0 22 24" fill="none" stroke="var(--brand-blue)" stroke-width="1.6"><rect x="3" y="5" width="16" height="14" rx="2"/><path d="M7 9h8M7 13h8M7 17h5"/></svg>Remove fluoride</li>
          <li><svg width="20" height="22" viewBox="0 0 22 24" fill="none" stroke="var(--brand-blue)" stroke-width="1.6"><rect x="6" y="3" width="10" height="18" rx="2"/><path d="M2 8h3M2 12h3M2 16h3M17 8h3M17 12h3M17 16h3"/></svg>Free filters for life</li>
        </ul>
      </div>

      <div class="call">
        <p class="lead">Call Trevor</p>
        <p class="number"><svg width="24" height="24" viewBox="0 0 28 28" aria-hidden="true"><circle cx="14" cy="14" r="13" fill="var(--band-blue)"/><path d="M9 7c1 0 2 3 2 4s-2 1-1 3 3 4 4 4 1-2 2-2 4 1 4 2-1 3-3 3C11 21 7 16 7 10c0-2 1-3 2-3z" fill="var(--white)"/></svg>0438 627 195</p>
      </div>
      <div class="web-pill">www.brightvalepipeworks.au</div>
      <div class="distributor"><p class="title">Authorised Distributor</p><p class="sub">Purestream Supply</p></div>
      <div class="social"><span>Follow us</span><span class="circle"></span><span class="circle"></span><span class="circle"></span></div>
    </section>
  </article>

  <!-- BACK -->
  <article class="flyer flyer--back">
    <section class="hero">
      <div class="product--back" role="img" aria-label="Product render of a stainless water filtration unit with three filter cartridges in white, blue and black, with a water splash"></div>
      <svg class="award award--back" width="66" height="66" viewBox="0 0 66 66" aria-hidden="true">
        <circle cx="33" cy="33" r="32" fill="var(--gold)"/>
        <circle cx="33" cy="33" r="25" fill="var(--gold-light)"/>
      </svg>
      <h1 class="back-headline display">
        <span class="blue">Your true<br>local</span><br>
        <span>Pipeworks &amp;<br>Boiler<br>Experts</span>
      </h1>
      <p class="service-area">We provide same day plumbing service<br>throughout the Illawarra, Wollongong,<br>Shellharbour &amp; Shoalhaven areas.</p>

      <div class="why-band">
        <div class="why-tab"><span>WHY<br>CHOOSE US?</span></div>
        <ul class="why-list">
          <li><span class="icon"><svg width="18" height="18" viewBox="0 0 20 20" fill="none" stroke="var(--ink)" stroke-width="1.5"><circle cx="10" cy="10" r="8"/><path d="M10 5v5l3 2"/></svg></span>Available<br>24/7</li>
          <li><span class="icon"><svg width="18" height="18" viewBox="0 0 20 20" fill="none" stroke="var(--ink)" stroke-width="1.5"><rect x="2" y="4" width="16" height="12" rx="1"/><path d="M5 8h4M5 12h4M12 8h3M12 12h3"/></svg></span>Fully<br>licensed<br>&amp; insured</li>
          <li><span class="icon"><svg width="18" height="18" viewBox="0 0 20 20" fill="none" stroke="var(--ink)" stroke-width="1.5"><circle cx="6" cy="7" r="2.5"/><circle cx="14" cy="7" r="2.5"/><path d="M2 17c0-3 2-5 4-5s4 2 4 5M10 17c0-3 2-5 4-5s4 2 4 5"/></svg></span>Family run<br>local<br>business</li>
          <li><span class="icon"><svg width="18" height="18" viewBox="0 0 20 20" fill="none" stroke="var(--ink)" stroke-width="1.5"><path d="M3 12l4-4 3 3 5-6M3 17h14"/></svg></span>Lifetime<br>labour<br>warranty</li>
          <li><span class="icon"><svg width="18" height="18" viewBox="0 0 20 20" fill="none" stroke="var(--ink)" stroke-width="1.5"><circle cx="10" cy="10" r="8"/><path d="M12.5 7c-.5-1-1.5-1.5-2.5-1.5-1.5 0-2.5.8-2.5 2s1 1.7 2.5 2 2.5.8 2.5 2-1 2-2.5 2c-1 0-2-.5-2.5-1.5M10 4v12"/></svg></span>Fixed<br>upfront<br>pricing</li>
        </ul>
      </div>
    </section>

    <section class="panel">
      <div class="benefit benefit--health">
        <h3>Health Benefits</h3>
        <div class="cols">
          <ul><li>Reduce the risk<br>of cancer</li><li>Relief for eczema<br>sufferers</li><li>Anti-Aging benefits</li><li>Reduce the risk of<br>birth defects</li></ul>
          <ul><li>Relief for<br>asthma sufferers</li><li>Enjoy chemical<br>free showering</li><li>Healthier<br>drinking water</li></ul>
        </div>
      </div>
      <div class="benefit benefit--remove">
        <h3>Remove &amp; Improve</h3>
        <div class="cols">
          <ul><li>Chlorine 99.99%</li><li>Chloramine 99.99%</li><li>Fluoride</li><li>Heavy Metals</li><li>Bacteria</li></ul>
          <ul><li>Parasites</li><li>Pesticides</li><li>Hard Water</li><li>PFA'S</li></ul>
        </div>
      </div>
      <div class="divider divider--left"></div>
      <div class="divider divider--right"></div>
      <div class="divider-v"></div>
      <div class="benefit benefit--extend">
        <h3>Extend the Life</h3>
        <div class="cols">
          <ul><li>Hot Water Systems</li><li>Washing machine</li><li>Dishwasher</li><li>Tapware</li></ul>
          <ul><li>Bathrooms</li><li>Plumbing</li><li>Home<br>appliances</li></ul>
        </div>
      </div>
      <div class="benefit benefit--world">
        <h3>World Leading</h3>
        <div class="cols">
          <ul><li>German Designed</li><li>100% Renewable</li><li>100% Sustainable</li><li>1000% Greater<br>Absorption</li></ul>
          <ul><li>Robust Design</li><li>Robust Warranty</li><li>Adopted<br>throughout Europe<br>and the USA</li></ul>
        </div>
      </div>

      <div class="call">
        <p class="lead">Call Trevor</p>
        <p class="number"><svg width="24" height="24" viewBox="0 0 28 28" aria-hidden="true"><circle cx="14" cy="14" r="13" fill="var(--band-blue)"/><path d="M9 7c1 0 2 3 2 4s-2 1-1 3 3 4 4 4 1-2 2-2 4 1 4 2-1 3-3 3C11 21 7 16 7 10c0-2 1-3 2-3z" fill="var(--white)"/></svg>0438 627 195</p>
      </div>
      <div class="web-pill">www.brightvalepipeworks.au</div>
      <div class="distributor"><p class="title">Authorised Distributor</p><p class="sub">Purestream Supply</p></div>
      <div class="social"><span>Follow us</span><span class="circle"></span><span class="circle"></span><span class="circle"></span></div>
    </section>
  </article>

</div>
</body>
</html>
```